Labour Day banner showcasing 20% off site

Banner graphic promoting our Labour Day sale
Size: 2000px x 600px
- examples from other companies and their sale banners have been uploaded for inspiration. Labour day examples are for the United States's holiday and submissions should NOT be in their country colours.
- product images can be found at www.tallpinegreens.com

Target Market(s)

19+

Industry/Entity Type

Cannabis

Requirements
Must have
• Phrases:
- “Happy Labour Day”
- “20% off site wide sale*"
- "Coupon code: Harvest20"
- Underneath phrase the date of sale “September 3rd - 7th”
- In tiny print “*excludes all sale and bundled items”
- MUST BE 2000px x 600px
Nice to have
• - images of the products or bud we carry which can be found at www.tallpinegreens.com
- bold
Should not have
• - company logo
- the American flag, we are a Canadian company, colours and flag should all be Canadian

```html
<!DOCTYPE html>
<html lang="en">
<head>
<meta charset="utf-8">
<title>Happy Labour Day – 20% off site wide sale</title>
<link rel="stylesheet" href="https://fonts.googleapis.com/css2?family=Poppins:ital,wght@0,400;0,500;0,600;0,700;1,800&family=Yellowtail&display=swap">
<style>
  :root {
    --red: #e3101b;
    --red-deep: #b8000a;
    --ink: #161616;
    --paper: #ffffff;
    --mist: #f3f3f3;
  }
  * { margin: 0; padding: 0; box-sizing: border-box; }
  html, body { width: 1200px; height: 360px; overflow: hidden; background: var(--paper); }
  .banner {
    position: relative;
    width: 1200px;
    height: 360px;
    overflow: hidden;
    background: var(--paper);
    font-family: "Poppins", sans-serif;
    color: var(--ink);
  }
  .flag-art, .bunting-art, .bottom-swoosh { position: absolute; display: block; }
  .flag-art { left: 0; top: 0; width: 560px; height: 220px; }
  .bunting-art { left: 690px; top: 0; width: 510px; height: 115px; }
  .bottom-swoosh { left: 0; top: 0; width: 1200px; height: 360px; }

  .product {
    position: absolute;
    border-radius: 6px;
  }
  .product--jelly-packs {
    left: 54px; top: 244px; width: 180px; height: 84px;
    background: linear-gradient(90deg, #e98a2c 0%, #e7c33a 30%, #6fae3e 60%, #e0405a 100%);
  }
  .product--sanitizers {
    left: 283px; top: 184px; width: 98px; height: 150px;
    background: linear-gradient(90deg, #3cc2b8 0%, #f2d33a 50%, #3a8fd6 100%);
    border-radius: 14px;
  }
  .product--cartridges {
    left: 862px; top: 200px; width: 82px; height: 130px;
    background: linear-gradient(180deg, #2b2b2b 0%, #1a1a1a 60%, #a48a3a 100%);
  }
  .product--concentrate-packs {
    left: 1006px; top: 163px; width: 152px; height: 166px;
    background: linear-gradient(160deg, #6a6fb8 0%, #3d4f8a 45%, #b94a3a 100%);
  }

  .headline {
    position: absolute;
    left: 0; width: 1200px;
    text-align: center;
  }
  .headline__happy {
    position: absolute;
    left: 566px; top: 38px;
    font-family: "Yellowtail", cursive;
    font-size: 30px;
    color: var(--ink);
    transform: rotate(-4deg);
  }
  .headline__title {
    position: absolute;
    left: 436px; top: 60px;
    font-weight: 700;
    font-size: 66px;
    letter-spacing: -1px;
    line-height: 1;
    color: var(--red);
  }
  .offer {
    position: absolute;
    left: 459px; top: 144px;
    white-space: nowrap;
    line-height: 1;
  }
  .offer__amount {
    font-weight: 800;
    font-style: italic;
    font-size: 36px;
    color: var(--red);
  }
  .offer__label {
    font-weight: 400;
    font-size: 24px;
    color: var(--ink);
    margin-left: 4px;
  }
  .ribbon { position: absolute; width: 48px; height: 66px; }
  .ribbon--left { left: 399px; top: 161px; }
  .ribbon--right { left: 772px; top: 161px; }

  .coupon {
    position: absolute;
    left: 467px; top: 206px;
    width: 282px; height: 38px;
    border-radius: 19px;
    background: linear-gradient(180deg, var(--red) 0%, var(--red-deep) 100%);
    color: var(--paper);
    font-size: 21px;
    font-weight: 500;
    display: flex; align-items: center; justify-content: center;
    white-space: nowrap;
  }
  .coupon__code { font-weight: 700; margin-left: 6px; }
  .sale-dates {
    position: absolute;
    left: 0; width: 1216px; top: 253px;
    text-align: center;
    font-weight: 600;
    font-size: 21px;
    color: var(--red);
  }
  .fine-print {
    position: absolute;
    left: 430px; top: 300px;
    font-size: 18px;
    font-weight: 400;
    color: var(--ink);
    white-space: nowrap;
  }
</style>
</head>
<body>
<main class="banner">
  <svg class="flag-art" viewBox="0 0 560 220" role="img" aria-label="Waving Canadian flag">
    <defs>
      <linearGradient id="flagTone" x1="0" y1="0" x2="1" y2="0">
        <stop offset="0" stop-color="#e3101b"/>
        <stop offset="0.18" stop-color="#e3101b"/>
        <stop offset="0.24" stop-color="#f4f4f4"/>
        <stop offset="0.6" stop-color="#eeeeee"/>
        <stop offset="0.68" stop-color="#e3101b"/>
        <stop offset="1" stop-color="#c8000c"/>
      </linearGradient>
    </defs>
    <path d="M0 0 H540 C430 40 330 60 260 110 C190 160 110 210 0 215 Z" fill="url(#flagTone)"/>
  </svg>

  <svg class="bunting-art" viewBox="0 0 510 115" role="img" aria-label="Red and white Canadian pennant bunting">
    <defs>
      <linearGradient id="buntingTone" x1="0" y1="0" x2="1" y2="0">
        <stop offset="0" stop-color="#f27a80"/>
        <stop offset="1" stop-color="#e3101b"/>
      </linearGradient>
    </defs>
    <path d="M0 0 L40 50 L90 80 L150 95 L210 105 L270 108 L330 104 L390 95 L450 75 L510 50 V0 Z" fill="url(#buntingTone)" opacity="0.55"/>
  </svg>

  <svg class="bottom-swoosh" viewBox="0 0 1200 360" aria-hidden="true">
    <path d="M860 360 C1000 352 1130 320 1200 268 V360 Z" fill="var(--red)"/>
    <rect x="0" y="353" width="1200" height="7" fill="var(--red)"/>
  </svg>

  <div class="product product--jelly-packs" role="img" aria-label="Fruit jelly edible packs in orange, mango, apple and cherry"></div>
  <div class="product product--sanitizers" role="img" aria-label="Three hand sanitizer bottles in silicone holders"></div>
  <div class="product product--cartridges" role="img" aria-label="Black and gold vape cartridge tubes"></div>
  <div class="product product--concentrate-packs" role="img" aria-label="Stack of concentrate packages"></div>

  <span class="headline__happy">Happy</span>
  <h1 class="headline__title">Labour Day</h1>

  <svg class="ribbon ribbon--left" viewBox="0 0 48 66" role="img" aria-label="Red ribbon flourish">
    <path d="M48 4 L6 14 L28 34 L4 62 L20 60 L36 36 L18 20 L46 16 Z" fill="var(--red)"/>
  </svg>
  <p class="offer"><span class="offer__amount">20% off</span><span class="offer__label">site wide sale</span></p>
  <svg class="ribbon ribbon--right" viewBox="0 0 48 66" role="img" aria-label="Red ribbon flourish">
    <path d="M0 4 L42 14 L20 34 L44 62 L28 60 L12 36 L30 20 L2 16 Z" fill="var(--red)"/>
  </svg>

  <div class="coupon">Coupon Code:<span class="coupon__code">Harvest20</span></div>
  <p class="sale-dates">September 3rd - 7th</p>
  <p class="fine-print">*excludes all sale and bundled items</p>
</main>
</body>
</html>
```